Homemaking training schools needs a Business Card design

Designer, Hello!

No special requirements, good-looking enough.
--------------------------------------------------------------------------

Name: Marcus Liao
Chairman
Tel: 0574-57418263
Mobile: 13852247106
Email: kelvory@mailpond.com
Web: www.tqb2031.com
Add: No.258, LinfengJie, DaoyueQu, Ningbo, Zhejiang

LOGO
Ningbo TQB Homemaking Training School

Target Market(s)

pregnant women, mothers, infants, the elderly and families, including cleaning, cooking, nursing training.

Industry/Entity Type

Business

Contact Information for Business Card

Name: Marcus Liao
Chairman
Tel: 0574-57418263
Mobile: 13852247106
Email: kelvory@mailpond.com
Web: www.tqb2031.com

LOGO

Font styles to use
Serif
Sans Serif
Decorative

Requirements
Nice to have
• Feels: clean, specifications, safety, comfort, warmth and happiness.

```html
<!DOCTYPE html>
<html lang="en">
<head>
<meta charset="utf-8">
<title>TianQiaoBao Business Card</title>
<link rel="stylesheet" href="https://fonts.googleapis.com/css2?family=Montserrat:wght@500;600&family=Open+Sans:wght@400&family=Quicksand:wght@500&display=swap">
<style>
  :root {
    --stage: #585858;
    --paper: #ffffff;
    --ink-dark: #000000;
    --brand-blue: #1f73be;
    --brand-pink: #e5117f;
    --text-grey: #4a4a4a;
    --rule-grey: #3d3d3d;
  }
  * { margin: 0; padding: 0; box-sizing: border-box; }
  html, body { width: 1105px; height: 1200px; overflow: hidden; }
  body { background: var(--stage); position: relative; }

  .card { position: absolute; left: 196px; width: 720px; height: 412px; }
  .card--front { top: 146px; background: var(--paper); }
  .card--back { top: 602px; background: var(--ink-dark); }

  .brand { position: absolute; left: 0; width: 100%; text-align: center; }
  .brand__name {
    position: absolute; left: 0; width: 100%;
    font-family: "Montserrat", sans-serif; font-weight: 600; color: var(--brand-blue);
    letter-spacing: -0.5px; line-height: 1;
  }
  .brand__tagline {
    position: absolute; left: 50%; transform: translateX(-50%);
    display: flex; align-items: center; white-space: nowrap;
    font-family: "Quicksand", sans-serif; font-weight: 500;
  }
  .brand__tagline::before, .brand__tagline::after { content: ""; display: block; height: 1.5px; }

  .card--front .brand__name { top: 104px; font-size: 40px; }
  .card--front .brand__tagline { top: 150px; font-size: 16px; color: var(--text-grey); gap: 8px; }
  .card--front .brand__tagline::before, .card--front .brand__tagline::after { width: 62px; background: var(--rule-grey); }

  .card--back .brand__name { top: 156px; font-size: 55px; }
  .card--back .brand__tagline { top: 228px; font-size: 23px; color: #ffffff; gap: 10px; }
  .card--back .brand__tagline::before, .card--back .brand__tagline::after { width: 90px; background: #ffffff; }

  .person { position: absolute; left: 0; width: 100%; top: 236px; text-align: center; font-family: "Montserrat", sans-serif; }
  .person__name { font-size: 27px; font-weight: 600; color: var(--brand-blue); line-height: 1; }
  .person__title-row { position: relative; margin: 6px 32px 0; height: 22px; }
  .person__title-row::before { content: ""; position: absolute; left: 0; right: 0; top: 12px; height: 1.5px; background: var(--brand-pink); }
  .person__title {
    position: relative; display: inline-block; padding: 0 4px; background: var(--paper);
    font-size: 20px; font-weight: 600; color: var(--brand-pink); line-height: 22px;
  }

  .contact { position: absolute; top: 313px; font-family: "Open Sans", sans-serif; font-size: 18px; color: var(--text-grey); line-height: 26px; font-style: normal; }
  .contact--address { left: 32px; }
  .contact--phones { left: 290px; }
  .contact--web { left: 462px; }
  .contact__row { display: flex; align-items: center; gap: 8px; white-space: nowrap; }
  .contact__icon { width: 18px; height: 18px; flex: none; fill: var(--brand-blue); }
</style>
</head>
<body>

<section class="card card--front">
  <div class="brand">
    <div class="brand__name">TianQiaoBao</div>
    <div class="brand__tagline">Training &amp; Services</div>
  </div>

  <div class="person">
    <div class="person__name">Marcus Liao</div>
    <div class="person__title-row"><span class="person__title">Chairman</span></div>
  </div>

  <address class="contact contact--address">
    <div class="contact__row">No.258, LinfengJie</div>
    <div class="contact__row">DaoyueQu, Ningbo, Zhejiang</div>
  </address>

  <div class="contact contact--phones">
    <div class="contact__row">
      <svg class="contact__icon" viewBox="0 0 24 24" aria-hidden="true"><path d="M6.6 10.8a15.1 15.1 0 0 0 6.6 6.6l2.2-2.2c.3-.3.7-.4 1-.2 1.1.4 2.3.6 3.6.6.6 0 1 .4 1 1V20c0 .6-.4 1-1 1A17 17 0 0 1 3 4c0-.6.4-1 1-1h3.5c.6 0 1 .4 1 1 0 1.3.2 2.5.6 3.6.1.3 0 .7-.2 1z"/></svg>
      <span>0574-57418263</span>
    </div>
    <div class="contact__row">
      <svg class="contact__icon" viewBox="0 0 24 24" aria-hidden="true"><path d="M7 1h10a2 2 0 0 1 2 2v18a2 2 0 0 1-2 2H7a2 2 0 0 1-2-2V3a2 2 0 0 1 2-2zm0 3v14h10V4z"/></svg>
      <span>13852247106</span>
    </div>
  </div>

  <div class="contact contact--web">
    <div class="contact__row">
      <svg class="contact__icon" viewBox="0 0 24 24" aria-hidden="true"><path d="M2 5h20v14H2zm2 2v.4l8 5.3 8-5.3V7zm0 2.8V17h16V9.8l-8 5.3z"/></svg>
      <span>kelvory@mailpond.com</span>
    </div>
    <div class="contact__row">
      <svg class="contact__icon" viewBox="0 0 24 24" aria-hidden="true"><path d="M12 2a10 10 0 1 0 0 20 10 10 0 0 0 0-20zm-1 17.9A8 8 0 0 1 4.1 10L9 15v1a2 2 0 0 0 2 2zm6.9-2.5A2 2 0 0 0 16 16h-1v-3a1 1 0 0 0-1-1H8v-2h2a1 1 0 0 0 1-1V7h2a2 2 0 0 0 2-2v-.4a8 8 0 0 1 2.9 12.8z"/></svg>
      <span>www.tqb2031.com</span>
    </div>
  </div>
</section>

<section class="card card--back">
  <div class="brand">
    <div class="brand__name">TianQiaoBao</div>
    <div class="brand__tagline">Training &amp; Services</div>
  </div>
</section>

</body>
</html>
```